Facial Tissue Brand Logo and Design

We would like you to design a Logo for the Facial Tissue Brand "Velora" along with the box design. The pack should indicate the pack size (150 x 2 ply). Also our company logo should be present (attached) along with a barcode. The box size dimensions should be 210mm (L) x 110mm (W) x 70mm (H). We are open to all kinds of nice designs which are attractive but not overdone. Happy designing!

UPDATE:
We appreciate the designs so far... but would also love to see more options in a simple and elegent design style that would look good on a table... please see attached below links for reference purpose:

www.pixmarrow.com/image-photo/cleaning-wipes-isolated-on-white-480215736

www.pixmarrow.com/image-photo/cleaning-wipes-isolated-on-white-692048153

www.pixmarrow.com/image-photo/delicate-female-hands-pulling-tissue-out-2875013649

Happy desgining!

We appreciate the designs so far.. but would like to to see some more options.

```html
<!DOCTYPE html>
<html lang="en">
<head>
<meta charset="utf-8">
<title>Velora Facial Tissue – Box Dieline</title>
<link rel="stylesheet" href="https://fonts.googleapis.com/css2?family=Montserrat:wght@300;400;600&display=swap">
<style>
  :root {
    --paper: #ffffff;
    --frame: #3a3a3a;
    --plum: #8a4f8a;
    --plum-deep: #6e3a6e;
    --fold: #5a2c5c;
    --cream: #f0eee8;
    --leaf: #8cc63f;
    --teal: #0fa08c;
    --blush: #e98fb8;
    --label: #ffffff;
    --mark: #3f7fb5;
  }
  html, body {
    margin: 0;
    padding: 0;
    overflow: hidden;
    background: var(--paper);
  }
  .canvas {
    width: 1200px;
    height: 800px;
    box-sizing: border-box;
    border: 1px solid var(--frame);
    background: var(--paper);
    overflow: hidden;
  }
  .dieline { display: block; }
  .panel { fill: var(--plum); }
  .flap { fill: var(--plum-deep); }
  .fold { stroke: var(--fold); stroke-width: 1.5; fill: none; }
  .band { fill: var(--cream); }
  .band-edge { stroke: var(--leaf); stroke-width: 6; }
  .window { fill: var(--cream); stroke: var(--leaf); stroke-width: 7; }
  .label-oval { fill: var(--label); }
  .brand {
    font-family: "Montserrat", sans-serif;
    font-weight: 600;
    fill: var(--teal);
  }
  .descriptor {
    font-family: "Montserrat", sans-serif;
    font-weight: 400;
    fill: var(--blush);
    letter-spacing: 2px;
  }
  .company {
    font-family: "Montserrat", sans-serif;
    font-weight: 300;
    fill: var(--label);
    font-size: 26px;
  }
  .country {
    font-family: "Montserrat", sans-serif;
    font-weight: 300;
    fill: var(--label);
    font-size: 9px;
    letter-spacing: 9px;
  }
  .company-square { fill: var(--mark); }
</style>
</head>
<body>
<div class="canvas">
  <svg class="dieline" width="1200" height="800" viewBox="95 80 1200 1410" preserveAspectRatio="xMidYMid meet" xmlns="http://www.w3.org/2000/svg">
    <defs>
      <linearGradient id="halftone-shade" x1="0" x2="1" y1="0" y2="0">
        <stop offset="0" stop-color="#74407a"/>
        <stop offset="0.18" stop-color="#8a4f8a"/>
        <stop offset="0.82" stop-color="#8a4f8a"/>
        <stop offset="1" stop-color="#74407a"/>
      </linearGradient>
    </defs>

    <!-- flaps: inner top panel -->
    <path class="flap" d="M313,105 L262,105 L200,128 Q193,131 193,140 L193,322 Q193,332 202,336 L262,360 L313,360 Z"/>
    <path class="flap" d="M1077,105 L1128,105 L1190,128 Q1197,131 1197,140 L1197,322 Q1197,332 1188,336 L1128,360 L1077,360 Z"/>

    <!-- flaps: side panels beside top face -->
    <path class="flap" d="M313,368 L137,378 Q125,379 125,391 L125,731 Q125,743 137,744 L313,752 Z"/>
    <path class="flap" d="M1077,368 L1253,378 Q1265,379 1265,391 L1265,731 Q1265,743 1253,744 L1077,752 Z"/>

    <!-- flaps: front panel -->
    <path class="flap" d="M313,762 L262,762 L200,785 Q193,788 193,797 L193,980 Q193,990 202,994 L262,1017 L313,1017 Z"/>
    <path class="flap" d="M1077,762 L1128,762 L1190,785 Q1197,788 1197,797 L1197,980 Q1197,990 1188,994 L1128,1017 L1077,1017 Z"/>

    <!-- flaps: bottom panel with locking notches -->
    <path class="flap" d="M313,1022 L262,1042 L210,1060 Q205,1062 205,1068 L205,1112 Q205,1122 195,1122 L135,1122 Q125,1122 125,1132 L125,1298 Q125,1308 135,1308 L195,1308 Q205,1308 205,1318 L205,1380 Q205,1386 212,1389 L313,1417 Z"/>
    <path class="flap" d="M1077,1022 L1128,1042 L1180,1060 Q1185,1062 1185,1068 L1185,1112 Q1185,1122 1195,1122 L1255,1122 Q1265,1122 1265,1132 L1265,1298 Q1265,1308 1255,1308 L1195,1308 Q1185,1308 1185,1318 L1185,1380 Q1185,1386 1178,1389 L1077,1417 Z"/>

    <!-- glue tab -->
    <path class="panel" d="M313,1417 L1077,1417 L1060,1465 L330,1465 Z"/>

    <!-- main column -->
    <g role="img" aria-label="Purple halftone dot pattern fading toward the centre of each panel">
      <rect x="313" y="105" width="764" height="1312" fill="url(#halftone-shade)"/>
    </g>

    <!-- inner top panel label (upside down) -->
    <g class="label inner-label" transform="rotate(180 700 225)">
      <ellipse class="label-oval" cx="700" cy="225" rx="148" ry="66"/>
      <text class="brand" x="700" y="235" font-size="58" text-anchor="middle">Velora</text>
      <text class="descriptor" x="700" y="268" font-size="15" text-anchor="middle">Facial Tissue</text>
    </g>

    <!-- top face with dispenser band -->
    <g class="top-face">
      <rect class="band" x="313" y="522" width="764" height="75"/>
      <line class="band-edge" x1="313" y1="522" x2="1077" y2="522"/>
      <line class="band-edge" x1="313" y1="597" x2="1077" y2="597"/>
      <ellipse class="window" cx="700" cy="560" rx="200" ry="98"/>
      <text class="brand" x="700" y="580" font-size="84" text-anchor="middle">Velora</text>
      <text class="descriptor" x="700" y="622" font-size="22" text-anchor="middle">Facial Tissue</text>
    </g>

    <!-- front panel label -->
    <g class="label front-label">
      <ellipse class="label-oval" cx="700" cy="886" rx="148" ry="66"/>
      <text class="brand" x="700" y="896" font-size="58" text-anchor="middle">Velora</text>
      <text class="descriptor" x="700" y="929" font-size="15" text-anchor="middle">Facial Tissue</text>
    </g>

    <!-- company on side flaps -->
    <g class="company-block company-left" transform="translate(272 405) rotate(90)">
      <rect class="company-square" x="0" y="0" width="66" height="66"/>
      <text class="company" x="86" y="36">NORVALE</text>
      <text class="company" x="86" y="62">TRADING</text>
      <text class="company" x="86" y="88">FZC</text>
      <text class="country" x="0" y="117">UNITED ARAB EMIRATES</text>
    </g>
    <g class="company-block company-right" transform="translate(1106 715) rotate(-90)">
      <rect class="company-square" x="0" y="0" width="66" height="66"/>
      <text class="company" x="86" y="52">NORVALE</text>
      <text class="company" x="86" y="78">TRADING</text>
      <text class="company" x="86" y="104">FZC</text>
      <text class="country" x="0" y="132">UNITED ARAB EMIRATES</text>
    </g>

    <!-- fold lines -->
    <g class="folds">
      <line class="fold" x1="313" y1="105" x2="313" y2="1417"/>
      <line class="fold" x1="1077" y1="105" x2="1077" y2="1417"/>
      <line class="fold" x1="313" y1="360" x2="1077" y2="360"/>
      <line class="fold" x1="313" y1="760" x2="1077" y2="760"/>
      <line class="fold" x1="313" y1="1017" x2="1077" y2="1017"/>
      <line class="fold" x1="313" y1="1417" x2="1077" y2="1417"/>
    </g>
  </svg>
</div>
</body>
</html>
```